Website Landing Page for Brightfall Systems

Create a custom designed website landing page for our business. Looking for a professional upscale design that incorporates our logo and logo colors into the theme. I want a standard fixed frame website, not a constant scrolling format that seems to be the trend. To start with I'm looking for more of the graphic design part, maybe a concept or theme, I don't expect to see a finished project. Not interested in generic templates or layouts.

The name of our company is Brightfall Systems and I've attached our logo below. I'd like to have the web page have the same look and feel of our logo, as well as the colors. Our company, Brightfall Systems does system design, installation, and programming, of residential and commercial Audio/Video and Automation systems. We do home theaters, lighting and building automation, video conferencing systems, security camera installations, conference rooms, projectors, distributed audio systems, and similar Technology projects. This will be a professional services/informational website. We will not sell products on this website. This website will be used to advertise our company and communicate our services to prospective customers. Having a well designed, professional and clean website is one way we want to distinguish our company from the competition.

Here are some examples of what I consider a professional well designed website
http://www.qorlamstudio.com/Work/

Last year we had our tradlo store designed (with PixelMarket) and I'm really happy with the way it turned out. You can see it at www.HolvenGearDepot.com I consider this to be a great design and looking for the same level of quality with this new website. However, do not copy or use any part of this design in this new project. This tradlo store is completely separate from our other company Brightfall Systems. I only mention this tradlo store an an example of good work.

Reason: Still going through designs.

Reason: Still working on project and have not had time to review all designs and request revisions.

Reason: Sill going through designs and requesting revisions

Reason: still going through all the submissions we received.

Target Market(s)

People interested in Audio/Video, home theaters, home automation. We do sales, system design, and programming. We typically work on larger projects with both residential and commercial customers.

Industry/Entity Type

Business

Number of Pages Required

1 page

Requirements
Must have
• Great design elements. Please use a white background. I think white goes well with our logo colors.

```html
<!DOCTYPE html>
<html lang="en">
<head>
<meta charset="utf-8">
<title>Brightfall Systems</title>
<link href="https://fonts.googleapis.com/css2?family=Roboto:wght@300;400;500&display=swap" rel="stylesheet">
<style>
  :root {
    --page-bg: #eef0f2;
    --site-bg: #ffffff;
    --ink: #1f2226;
    --ink-soft: #3a3e44;
    --muted: #8a9097;
    --brand-blue: #1f8fd6;
    --brand-green: #5cbf3a;
    --button-blue: #1e74f0;
    --rule: #e6e8eb;
    --hero-grey: #eceeef;
  }
  * { box-sizing: border-box; margin: 0; padding: 0; }
  html, body { width: 1200px; height: 1200px; overflow: hidden; }
  body {
    background: var(--page-bg);
    font-family: "Roboto", Arial, sans-serif;
    color: var(--ink);
    position: relative;
  }
  .site {
    position: absolute; left: 0; top: 238px;
    width: 1200px; height: 723px;
    background: var(--site-bg);
    overflow: hidden;
  }
  .site-header {
    position: absolute; left: 0; top: 0; width: 100%; height: 127px;
    border-bottom: 1px solid var(--rule);
    background: var(--site-bg);
  }
  .brand { position: absolute; left: 114px; top: 32px; height: 64px; display: flex; align-items: center; gap: 16px; }
  .brand-mark { width: 64px; height: 64px; border-radius: 50%; border: 4px solid var(--brand-blue); }
  .brand-name {
    font-size: 24px; font-weight: 500; letter-spacing: 1px;
    text-transform: uppercase; color: var(--brand-blue);
  }
  .main-nav { position: absolute; top: 60px; left: 0; width: 100%; font-size: 13px; font-weight: 500; }
  .main-nav a { position: absolute; color: var(--ink); text-decoration: none; white-space: nowrap; }
  .main-nav a.is-active::after {
    content: ""; position: absolute; left: 5px; top: 29px; width: 34px; height: 2px; background: var(--brand-green);
  }
  .main-nav a.nav-cta { color: var(--muted); font-weight: 400; }
  .hero {
    position: absolute; left: 0; top: 128px; width: 100%; height: 442px;
    background:
      linear-gradient(180deg, rgba(255,255,255,0) 60%, var(--site-bg) 100%),
      linear-gradient(120deg, #e3e5e7 0%, var(--hero-grey) 35%, #f4f5f6 60%, #e9ebec 100%);
  }
  .hero-title {
    position: absolute; left: 114px; top: 99px; width: 420px;
    font-size: 28px; font-weight: 300; line-height: 33px; color: var(--ink);
  }
  .hero-text {
    position: absolute; left: 116px; top: 282px; width: 420px;
    font-size: 15px; line-height: 21px; color: var(--ink);
  }
  .hero-button {
    position: absolute; left: 116px; top: 377px; width: 178px; height: 42px;
    border-radius: 21px; background: var(--button-blue); color: #fff;
    font-size: 13px; display: flex; align-items: center; justify-content: center; gap: 10px;
    text-decoration: none; box-shadow: 0 4px 10px rgba(30,116,240,0.25);
  }
  .gallery-tile { position: absolute; }
  .tile-theater { left: 600px; top: 155px; width: 242px; height: 151px; background: linear-gradient(160deg, #4a4640, #8b8478 45%, #2c2b2e); }
  .tile-tower { left: 851px; top: 155px; width: 247px; height: 151px; background: linear-gradient(135deg, #3b6fc9, #8fb3e6 50%, #c9d6e6); }
  .tile-boardroom { left: 600px; top: 315px; width: 242px; height: 152px; background: linear-gradient(180deg, #8a5a4a, #5c4038 45%, #b8bcc0); }
  .tile-lounge { left: 851px; top: 315px; width: 247px; height: 152px; background: linear-gradient(160deg, #e7dcc6, #c9b28e 50%, #8f7b62); }
  .tile-bar { left: 600px; top: 476px; width: 242px; height: 149px; background: linear-gradient(170deg, #2f2a26, #6b4a32 55%, #a06a3e); }
  .tile-villa { left: 853px; top: 476px; width: 245px; height: 149px; background: linear-gradient(180deg, #1a3fa8, #203a7a 50%, #a07a4a); }
  .site-footer {
    position: absolute; left: 0; top: 668px; width: 100%; height: 55px;
    border-top: 1px solid var(--rule);
  }
  .copyright { position: absolute; left: 161px; top: 22px; font-size: 10px; color: var(--muted); }
  .contact-line { position: absolute; left: 805px; top: 19px; font-size: 13px; color: var(--ink-soft); display: flex; align-items: center; gap: 9px; }
  .social-dot { width: 9px; height: 9px; border-radius: 50%; background: var(--button-blue); display: inline-block; }
  .back-to-top {
    position: absolute; left: 1004px; top: 11px; width: 34px; height: 34px;
    background: var(--button-blue); display: flex; align-items: center; justify-content: center;
  }
</style>
</head>
<body>
  <div class="site">
    <header class="site-header">
      <div class="brand">
        <span class="brand-mark"></span>
        <span class="brand-name">Brightfall Systems</span>
      </div>
      <nav class="main-nav">
        <a href="#" style="left:617px">Services</a>
        <a href="#" style="left:708px">Work</a>
        <a href="#" class="is-active" style="left:795px">About</a>
        <a href="#" style="left:879px">Contact</a>
        <a href="#" class="nav-cta" style="left:959px">Start a Project</a>
      </nav>
    </header>

    <section class="hero">
      <h1 class="hero-title">System design, installation, and programming, of residential and commercial Audio/Video and Automation systems</h1>
      <p class="hero-text">We do home theaters, lighting and building automation, security camera installations, projectors, distributed audio systems and similar projects.</p>
      <a href="#" class="hero-button">Discover more
        <svg width="10" height="8" viewBox="0 0 10 8"><path d="M0 4h8M5.5 1.5 8 4 5.5 6.5" stroke="#fff" stroke-width="1.2" fill="none"/></svg>
      </a>
    </section>

    <div class="gallery-tile tile-theater" role="img" aria-label="Photo of a large auditorium with a projection screen and tiered seating"></div>
    <div class="gallery-tile tile-tower" role="img" aria-label="Photo of a glass office building under a blue sky"></div>
    <div class="gallery-tile tile-boardroom" role="img" aria-label="Photo of a conference room with a long table and wall displays"></div>
    <div class="gallery-tile tile-lounge" role="img" aria-label="Photo of a bright living room with a media wall and ceiling projector"></div>
    <div class="gallery-tile tile-bar" role="img" aria-label="Photo of a restaurant bar with stools and pendant lights"></div>
    <div class="gallery-tile tile-villa" role="img" aria-label="Photo of a lit residence with palm trees at dusk"></div>

    <footer class="site-footer">
      <p class="copyright">© Copyright 2017 Studio Northcrest, All Rights Reserved</p>
      <div class="contact-line">
        <span>Get in touch:</span>
        <span class="social-dot"></span>
        <span class="social-dot"></span>
        <span class="social-dot"></span>
        <span class="social-dot"></span>
        <span class="social-dot"></span>
      </div>
      <a href="#" class="back-to-top" aria-label="Back to top">
        <svg width="10" height="6" viewBox="0 0 10 6"><path d="M1 5 5 1 9 5" stroke="#fff" stroke-width="1.6" fill="none"/></svg>
      </a>
    </footer>
  </div>
</body>
</html>
```